Business Cards and Stationary For Home Automation Company
based on recently completed logo
Business Cards and Stationary For Home Automation Company  - Manufacturing
Creative Brief
Professional
Milo Brandt
VP - Product and Business Development
717 Larkfield Crest Avenue Suite K310 Piscataway, NJ 08821
milo@mybrightwaterdwellingtech.com
www.MyBrightwaterDwellingTech.com

```html
<!DOCTYPE html>
<html lang="en">
<head>
<meta charset="utf-8">
<title>Brightwater Dwelling Tech – Business Card</title>
<link href="https://fonts.googleapis.com/css2?family=Open+Sans:wght@400;600;800&display=swap" rel="stylesheet">
<style>
  :root {
    --page-bg: #d9d6d2;
    --card-bg: #f7f7f5;
    --ink: #2b2b2b;
    --ink-soft: #555555;
    --green: #5cbf1f;
    --band-dark: #151515;
    --white: #ffffff;
  }
  * { margin: 0; padding: 0; box-sizing: border-box; }
  html, body {
    width: 1200px; height: 768px; overflow: hidden;
    background: var(--page-bg);
    font-family: "Open Sans", Arial, sans-serif;
  }
  .card {
    position: absolute; left: 100px; top: 98px;
    width: 1000px; height: 572px;
    background: var(--card-bg);
    border-radius: 6px;
    box-shadow: 0 18px 40px rgba(0,0,0,0.18);
    overflow: hidden;
    color: var(--ink);
  }
  .brand {
    position: absolute; left: 450px; top: 80px;
    display: flex; align-items: center; gap: 22px;
  }
  .brand-mark {
    width: 110px; height: 110px; border-radius: 50%;
    background: var(--ink);
  }
  .brand-name {
    font-weight: 800; font-size: 46px; line-height: 1.02;
    color: var(--ink); letter-spacing: -0.5px;
  }
  .person-name {
    position: absolute; left: 76px; top: 208px;
    font-size: 44px; font-weight: 600; color: var(--green);
  }
  .name-rule {
    position: absolute; left: 0; top: 275px;
    width: 720px; height: 3px; background: var(--green);
  }
  .person-title {
    position: absolute; left: 76px; top: 306px;
    width: 440px;
    font-size: 30px; line-height: 40px; font-weight: 400; color: var(--ink-soft);
  }
  .contact {
    position: absolute; right: 54px; top: 328px;
    text-align: right; font-size: 22px; line-height: 36px; color: var(--ink);
  }
  .contact li { list-style: none; display: flex; justify-content: flex-end; align-items: center; gap: 10px; }
  .contact .address { display: block; max-width: 440px; line-height: 32px; margin-bottom: 6px; }
  .contact svg { width: 22px; height: 22px; flex: none; }
  .band-green {
    position: absolute; left: 340px; right: 0; bottom: 0;
    height: 40px; background: var(--green);
  }
  .band-dark {
    position: absolute; left: 0; bottom: 0;
    width: 430px; height: 56px; background: var(--band-dark);
    border-top-right-radius: 60px 56px;
    display: flex; align-items: center; padding-left: 36px;
    color: var(--white); font-size: 19px;
  }
</style>
</head>
<body>
  <div class="card">
    <div class="brand">
      <div class="brand-mark"></div>
      <div class="brand-name">Brightwater<br>Dwelling<br>Tech</div>
    </div>

    <div class="person-name">Milo Brandt</div>
    <div class="name-rule"></div>
    <div class="person-title">VP - Product and<br>Business Development</div>

    <ul class="contact">
      <li class="address">717 Larkfield Crest Avenue Suite K310 Piscataway, NJ 08821</li>
      <li>012 555 0147
        <svg viewBox="0 0 22 22" aria-hidden="true"><circle cx="11" cy="11" r="11" fill="var(--green)"/><path d="M7 6c1-1 2 0 2.5 1.5s-.5 1.5-.5 2.5 2 3 3 3 1.2-1 2.5-.5 2.5 1.5 1.5 2.5-3 1-6-2-4-6-3-7z" fill="#fff"/></svg>
      </li>
      <li>milo@mybrightwaterdwellingtech.com
        <svg viewBox="0 0 22 22" aria-hidden="true"><circle cx="11" cy="11" r="11" fill="var(--green)"/><rect x="5" y="7" width="12" height="8" fill="#fff"/><path d="M5 7l6 5 6-5" fill="none" stroke="var(--green)" stroke-width="1.3"/></svg>
      </li>
      <li>www.MyBrightwaterDwellingTech.com
        <svg viewBox="0 0 22 22" aria-hidden="true"><circle cx="11" cy="11" r="11" fill="var(--green)"/><circle cx="11" cy="11" r="6" fill="none" stroke="#fff" stroke-width="1.4"/><path d="M5 11h12M11 5c-3 3-3 9 0 12M11 5c3 3 3 9 0 12" fill="none" stroke="#fff" stroke-width="1.2"/></svg>
      </li>
    </ul>

    <div class="band-green"></div>
    <div class="band-dark">www.MyBrightwaterDwellingTech.com</div>
  </div>
</body>
</html>
```